Copper Ridge Business Cards For New Startup

I am looking for you to design some business cards for a new startup https://copperridgehub.example. I have supplied logo, brand guidelines and our signatures as a guide.

We need this to reflect the brand guidelines and the website for brand consistency,

What is Copper Ridge?

Mallorca's Business Growth Community
Join your new business community full of passionate entrepreneurs who
love to solve problems and help each other grow together!

Any questions you can ask.

Target Market(s)

Business to Business

Contact Information for Business Card

These are attached (signatures) to the job

Font styles to use
Other font styles liked:
• Open Sans

Requirements
Must have
• Match design guidelines
Nice to have
• Photos of our faces so people remember us

```html
<!DOCTYPE html>
<html lang="en">
<head>
<meta charset="utf-8">
<title>Copper Ridge Business Card</title>
<link href="https://fonts.googleapis.com/css2?family=Lato:wght@400;700&display=swap" rel="stylesheet">
<style>
  :root {
    --backdrop: #8c8c8c;
    --card-white: #ffffff;
    --brand-olive: #666600;
    --brand-olive-dark: #575700;
    --text-grey: #6b6b6b;
    --photo-light: #b9a48e;
    --photo-dark: #4f5a3a;
    --card-shadow: rgba(0, 0, 0, 0.45);
  }
  html, body {
    margin: 0;
    padding: 0;
    width: 1200px;
    height: 900px;
    overflow: hidden;
    background: var(--backdrop);
    font-family: "Lato", sans-serif;
  }
  .canvas {
    position: relative;
    width: 1200px;
    height: 900px;
  }
  .card {
    position: absolute;
    top: 200px;
    width: 310px;
    height: 502px;
    box-shadow: 3px 4px 5px var(--card-shadow);
  }
  .card--front {
    left: 253px;
    background: var(--card-white);
    border-radius: 56px 0 56px 0;
  }
  .card--back {
    left: 627px;
    background: var(--brand-olive);
    border-radius: 0 56px 0 56px;
  }
  .portrait {
    position: absolute;
    left: 42px;
    top: 42px;
    width: 226px;
    height: 226px;
    border-radius: 50%;
    background:
      radial-gradient(circle at 50% 42%, var(--photo-light) 0 26%, transparent 27%),
      radial-gradient(ellipse at 50% 100%, var(--photo-dark) 0 34%, transparent 35%),
      var(--brand-olive);
  }
  .identity {
    position: absolute;
    left: 32px;
    top: 306px;
  }
  .identity__name {
    margin: 0;
    font-size: 18px;
    font-weight: 700;
    color: var(--brand-olive-dark);
    letter-spacing: 0.1px;
    line-height: 22px;
  }
  .identity__role,
  .identity__company {
    margin: 0;
    font-size: 14px;
    color: var(--text-grey);
    line-height: 18px;
  }
  .contact-list {
    position: absolute;
    left: 32px;
    top: 375px;
    margin: 0;
    padding: 0;
    list-style: none;
  }
  .contact-list__item {
    display: flex;
    align-items: center;
    gap: 5px;
    font-size: 14px;
    color: var(--text-grey);
    line-height: 18.5px;
  }
  .contact-list__icon {
    width: 12px;
    height: 12px;
    fill: var(--brand-olive);
  }
  .social-row {
    position: absolute;
    left: 34px;
    top: 449px;
    display: flex;
    gap: 4px;
  }
  .social-row__dot {
    width: 16px;
    height: 16px;
    border: 1.3px solid var(--brand-olive);
    border-radius: 50%;
  }
  .wordmark {
    position: absolute;
    left: 136px;
    top: 82px;
    height: 240px;
    writing-mode: vertical-rl;
    transform: rotate(180deg);
    text-align: center;
    font-size: 31px;
    font-weight: 700;
    letter-spacing: 1px;
    color: var(--card-white);
    white-space: nowrap;
  }
  .brand-circle {
    position: absolute;
    left: 122px;
    top: 347px;
    width: 62px;
    height: 62px;
    border: 2.5px solid var(--card-white);
    border-radius: 50%;
  }
</style>
</head>
<body>
<main class="canvas">
  <section class="card card--front">
    <div class="portrait" role="img" aria-label="Portrait photo of Marcus Delaney on an olive green circle"></div>

    <div class="identity">
      <p class="identity__name">MARCUS DELANEY</p>
      <p class="identity__role">Founder &amp; Growth Hacker</p>
      <p class="identity__company">Copper Ridge</p>
    </div>

    <ul class="contact-list">
      <li class="contact-list__item">
        <svg class="contact-list__icon" viewBox="0 0 12 12" aria-hidden="true">
          <path d="M1 4.5 Q6 1 11 4.5 L9.5 6 L8 5 L8 4 Q6 3.3 4 4 L4 5 L2.5 6 Z"/>
          <rect x="2.5" y="6.5" width="7" height="4" rx="1"/>
        </svg>
        +34 600 555 210
      </li>
      <li class="contact-list__item">
        <svg class="contact-list__icon" viewBox="0 0 12 12" aria-hidden="true">
          <rect x="1" y="2.5" width="10" height="7"/>
          <path d="M1.5 3 L6 6.5 L10.5 3" fill="none" stroke="#fff" stroke-width="1"/>
        </svg>
        md@copperridgehub.example
      </li>
      <li class="contact-list__item">
        <svg class="contact-list__icon" viewBox="0 0 12 12" aria-hidden="true">
          <circle cx="6" cy="6" r="5"/>
          <path d="M3 3.5 Q5 4 4.5 6 Q6 7 5.5 9.5 M7.5 2.5 Q7 4.5 9 5" fill="none" stroke="#fff" stroke-width="0.9"/>
        </svg>
        copperridgehub.example
      </li>
    </ul>

    <div class="social-row" aria-label="Social profiles">
      <span class="social-row__dot"></span>
      <span class="social-row__dot"></span>
      <span class="social-row__dot"></span>
      <span class="social-row__dot"></span>
      <span class="social-row__dot"></span>
    </div>
  </section>

  <section class="card card--back">
    <div class="wordmark">COPPER RIDGE</div>
    <span class="brand-circle" aria-hidden="true"></span>
  </section>
</main>
</body>
</html>
```